We require a business card that promotes our Electrical business. Things we would like included are;
1) our business name, Bright Path Electrical and Communication
2) Our Electrical licence, EC 27036
3) Our ABN, 52 147 906 318
4) Our website, www.ridgewirecrew.com.au
5) Our Email, info@ridgewirecrew.com.au
6) Our contact number, 0452 681 207
7) Our address, 48 Marlow Rd Tandridge Perth 6093
8) Our logo, I will attach this (can you please change it so the ackground is white not black)
9) Our colours are red and white and perhaps some black
10) Managing Director Dorian Velcourt
11) the back to say 'notes' and have some lines for writing

Target Market(s)

General

Industry/Entity Type

Electrical

Contact Information for Business Card

Include the colour white, black and red.

Font styles to use
Sans Serif

Requirements
Nice to have
• A thunder bolt or a power point or a cord or something electrical, cartoon image of a cartoon like electrical tradie

```html
<!DOCTYPE html>
<html lang="en">
<head>
<meta charset="utf-8">
<title>Bright Path Electrical and Communication – Business Card</title>
<link href="https://fonts.googleapis.com/css2?family=Open+Sans:wght@400;600;700&display=swap" rel="stylesheet">
<style>
  :root {
    --red: #e0262f;
    --red-deep: #c81f27;
    --white: #ffffff;
    --paper: #f3f3f3;
    --ink: #1a1a1a;
    --rule: #2b2b2b;
    --backdrop: #e6e4e1;
  }
  * { box-sizing: border-box; margin: 0; padding: 0; }
  html, body {
    width: 1200px; height: 780px; overflow: hidden;
    background: var(--backdrop);
    font-family: "Open Sans", Arial, sans-serif;
    color: var(--ink);
  }
  .sheet {
    width: 1200px; height: 780px;
    display: flex; align-items: center; justify-content: center; gap: 40px;
  }
  .card {
    width: 540px; height: 330px;
    background: linear-gradient(180deg, var(--white), var(--paper));
    box-shadow: 0 6px 18px rgba(0,0,0,.18);
    display: flex; flex-direction: column;
    overflow: hidden;
  }
  .band {
    background: var(--red);
    color: var(--white);
    display: flex; flex-direction: column; justify-content: center;
  }
  .band--top { height: 104px; padding: 0 28px; border-bottom: 3px solid var(--rule); }
  .band--bottom { height: 50px; padding: 0 28px; border-top: 3px solid var(--rule); background: var(--red-deep); }
  .company-name { font-size: 33px; font-weight: 600; line-height: 1.05; letter-spacing: .2px; }
  .company-sub { font-size: 24px; font-weight: 600; line-height: 1.1; padding-left: 120px; }
  .front-body { flex: 1; display: flex; align-items: center; padding: 0 28px; gap: 28px; }
  .brand-spot {
    width: 150px; display: flex; align-items: center; gap: 8px;
    color: var(--red); font-weight: 700; font-size: 20px; line-height: 1.1;
  }
  .brand-spot .dot { width: 18px; height: 18px; border-radius: 50%; background: var(--red); flex: none; }
  .contact { font-size: 14px; line-height: 1.45; }
  .contact .person { color: var(--red); font-weight: 700; font-size: 20px; line-height: 1.1; }
  .contact .role { font-size: 13px; margin-bottom: 8px; }
  .contact .row { display: flex; align-items: center; gap: 6px; }
  .contact .icon { width: 14px; height: 14px; flex: none; }
  .contact .label { color: var(--red); }
  .address { font-size: 15px; font-weight: 600; letter-spacing: .3px; }
  .back-body { flex: 1; position: relative; padding: 22px 34px 18px; }
  .notes-title { text-align: right; font-size: 22px; font-weight: 400; margin-bottom: 10px; }
  .note-line { height: 1px; background: var(--rule); margin-top: 29px; }
  .website { font-size: 15px; font-weight: 400; letter-spacing: .3px; }
</style>
</head>
<body>
<main class="sheet">
  <section class="card card--front" aria-label="Card front">
    <header class="band band--top">
      <div class="company-name">Bright Path Electrical</div>
      <div class="company-sub">and Communication</div>
    </header>
    <div class="front-body">
      <div class="brand-spot"><span class="dot"></span><span>Bright Path</span></div>
      <div class="contact">
        <div class="person">Dorian Velcourt</div>
        <div class="role">Managing Director</div>
        <div class="row">
          <svg class="icon" viewBox="0 0 14 14" aria-hidden="true"><rect width="14" height="14" rx="2" fill="var(--red)"/><path d="M4 3.5l1.6-.4 1 2-1 .8a5 5 0 0 0 2.5 2.5l.8-1 2 1-.4 1.6C7.5 10.5 3.5 6.5 4 3.5z" fill="#fff"/></svg>
          <span>0452 681 207</span>
        </div>
        <div class="row">
          <svg class="icon" viewBox="0 0 14 14" aria-hidden="true"><rect width="14" height="14" rx="2" fill="var(--red)"/><rect x="3" y="4" width="8" height="6" fill="none" stroke="#fff" stroke-width="1"/><path d="M3 4l4 3.2L11 4" fill="none" stroke="#fff" stroke-width="1"/></svg>
          <span>info@ridgewirecrew.com.au</span>
        </div>
        <div class="row"><span><span class="label">ABN</span> 52 147 906 318</span></div>
        <div class="row"><span>Electrical licence&nbsp; EC 27036</span></div>
      </div>
    </div>
    <footer class="band band--bottom">
      <div class="address">48 Marlow Rd Tandridge Perth 6093</div>
    </footer>
  </section>

  <section class="card card--back" aria-label="Card back">
    <div class="back-body">
      <div class="notes-title">Notes</div>
      <div class="note-line"></div>
      <div class="note-line"></div>
      <div class="note-line"></div>
      <div class="note-line"></div>
      <div class="note-line"></div>
    </div>
    <footer class="band band--bottom">
      <div class="website">www.ridgewirecrew.com.au</div>
    </footer>
  </section>
</main>
</body>
</html>
```